Business Card Design, including supply of raw art files plus a vector diagram of the flenzo logo and

We need the business card design for a company that is launching a new exciting product. The brief requires the submission of the following once the final design is chosen:

- business card layout including raw files
- a composite vector image file of the flenzo logo and tag line
- a standalone vector image file of the flenzo logo

The product will be launched as a customer engagement app.

It has 4 core modules which enables a person to do multiple things - book tours and activities, order takeaways, search for local deals and offers. A universal currency is at the heart of this product. When you use the app, you earn cashback rewards when shopping or buying at any of the merchant partners across the modules as . These rewards can then be used as full or part payment when buying goods or services at these merchant partners.

The business card must help us build the brand, communicate the benefit of the brand's key focus - the ability to earn and burn this universal cashback ccurrency - across the 4 modules - booking of tours and activities, ordering, searching for local deals and payment.

We would like the design to use the brand's blue colour the hex colour is: 00
Dark grey : 646464
Darker blue shadow: 058bdd
Main Blue: 0084ff

We need to translate this into a CMYK print or spot colour print.

Both print options to be supplied as separate files.

An example of the base concept we have in mind is attached for your reference.

The font used by the brand is Proxima Nova.

Industry/Entity Type

Business

Contact Information for Business Card

Carla Whitfield
Marketing
W: www.flenzo.co
M: + 61 407318265
T: +61 2 9375 4120
A: Suite 7, Level 2, 14-18 Harrow Lane, Sydney, NSW, 2000, Australia

Font styles to use
Sans Serif

Requirements
Must have
• flEnzo logo and tagline
• address details
• flEnzo icons as supplied
Nice to have
• would like to have the option of a spot varnish layer over the logo and icons at the back of the card

```html
<!DOCTYPE html>
<html lang="en">
<head>
<meta charset="utf-8">
<title>flEnzo Business Card</title>
<link rel="stylesheet" href="https://fonts.googleapis.com/css2?family=Roboto:wght@100;300;400;500;700&display=swap">
<style>
  :root {
    --stage: #5a5a5a;
    --card-blue: #0a86d8;
    --mark-blue: #00a0ef;
    --name-blue: #1a86d0;
    --white: #ffffff;
    --grey: #8a8a8a;
    --dark-grey: #646464;
  }
  * { margin: 0; padding: 0; box-sizing: border-box; }
  html, body {
    width: 1200px; height: 1000px; overflow: hidden;
    background: var(--stage);
    font-family: "Roboto", Arial, sans-serif;
  }
  .card { position: absolute; left: 220px; width: 761px; }
  .card-front { top: 50px; height: 434px; background: var(--card-blue); color: var(--white); }
  .card-back { top: 524px; height: 436px; background: var(--white); }

  .brand-disc {
    position: absolute; left: 153px; top: 98px;
    width: 114px; height: 114px; border-radius: 50%; background: var(--white);
  }
  .brand-lockup {
    position: absolute; left: 310px; top: 84px;
    display: inline-block;
  }
  .brand-name {
    display: block;
    font-weight: 100; font-size: 92px; line-height: 1; letter-spacing: 4px;
  }
  .brand-tagline {
    display: block; text-align: right; margin-top: 4px;
    font-weight: 300; font-size: 26px; line-height: 30px; letter-spacing: 0.3px;
    white-space: nowrap;
  }
  .modules { position: absolute; top: 320px; left: 0; width: 100%; }
  .module { position: absolute; width: 130px; text-align: center; }
  .module svg { display: block; margin: 0 auto; width: 46px; height: 46px; }
  .module-label { display: block; margin-top: 12px; font-size: 11px; font-weight: 500; }

  .back-disc {
    position: absolute; left: 96px; top: 104px;
    width: 228px; height: 228px; border-radius: 50%;
    background: var(--mark-blue);
    display: flex; align-items: center; justify-content: center;
  }
  .back-disc-name { color: var(--white); font-weight: 300; font-size: 48px; }
  .divider {
    position: absolute; left: 347px; top: 116px;
    width: 2px; height: 205px; background: var(--name-blue);
  }
  .contact { position: absolute; left: 369px; top: 111px; color: var(--grey); }
  .contact-name { font-size: 23px; font-weight: 700; color: var(--name-blue); line-height: 28px; letter-spacing: 0.3px; }
  .contact-role { font-size: 17px; line-height: 22px; }
  .contact-address { margin-top: 13px; font-size: 17px; line-height: 22px; }
  .contact-list { list-style: none; margin-top: 10px; }
  .contact-list li { display: flex; align-items: center; font-size: 17px; line-height: 24.5px; }
  .contact-list svg { width: 13px; height: 13px; margin-right: 7px; fill: var(--name-blue); }
</style>
</head>
<body>

<section class="card card-front">
  <div class="brand-disc"></div>
  <div class="brand-lockup">
    <span class="brand-name">flEnzo</span>
    <span class="brand-tagline">earn it, spend it local</span>
  </div>

  <div class="modules">
    <div class="module" style="left:135px">
      <svg viewBox="0 0 46 46" fill="#fff">
        <circle cx="23" cy="23" r="10"/>
        <text x="23" y="28" text-anchor="middle" font-size="13" font-weight="700" fill="#0a86d8" font-family="Roboto, sans-serif">$</text>
        <path d="M6 14 a14 14 0 0 1 16 -8 l0 -4 l7 7 l-7 7 l0 -4 a9 9 0 0 0 -10 5z"/>
        <path d="M40 32 a14 14 0 0 1 -16 8 l0 4 l-7 -7 l7 -7 l0 4 a9 9 0 0 0 10 -5z"/>
      </svg>
      <span class="module-label">CashBack Rewards</span>
    </div>
    <div class="module" style="left:272px">
      <svg viewBox="0 0 46 46">
        <path fill="#fff" d="M4 13 h10 l4 -5 h10 l4 5 h10 v25 h-38z"/>
        <circle cx="23" cy="25" r="9" fill="none" stroke="#0a86d8" stroke-width="3"/>
      </svg>
      <span class="module-label">Tours &amp; Activities</span>
    </div>
    <div class="module" style="left:401px">
      <svg viewBox="0 0 46 46" stroke="#fff" stroke-width="3" fill="none" stroke-linecap="round">
        <path d="M10 42 L34 14"/>
        <ellipse cx="36" cy="9" rx="4" ry="6" fill="#fff" transform="rotate(40 36 9)"/>
        <path d="M36 42 L14 16"/>
        <path d="M9 4 v8 a5 5 0 0 0 10 0 v-8 M14 4 v10" stroke-width="2"/>
      </svg>
      <span class="module-label">Mobile Ordering</span>
    </div>
    <div class="module" style="left:515px">
      <svg viewBox="0 0 46 46">
        <path fill="#fff" d="M24 4 h16 v16 l-20 20 l-16 -16z"/>
        <circle cx="34" cy="10" r="3" fill="#0a86d8"/>
      </svg>
      <span class="module-label">Local Offers</span>
    </div>
  </div>
</section>

<section class="card card-back">
  <div class="back-disc"><span class="back-disc-name">flEnzo</span></div>
  <div class="divider"></div>
  <div class="contact">
    <div class="contact-name">Carla Whitfield</div>
    <div class="contact-role">Marketing</div>
    <div class="contact-address">Suite 7, Level 2, 14-18 Harrow<br>Lane, Sydney NSW 2000</div>
    <ul class="contact-list">
      <li><svg viewBox="0 0 13 13"><path d="M3.5 0 h6 v13 h-6z M4.5 1.5 v8.5 h4 v-8.5z"/></svg>+61 407 318 265</li>
      <li><svg viewBox="0 0 13 13"><path d="M3 1 l3 3 l-2 2 a8 8 0 0 0 3 3 l2 -2 l3 3 l-2 2 a11 11 0 0 1 -9 -9z"/></svg>+61 2 9375 4120</li>
      <li><svg viewBox="0 0 13 13"><path d="M0 2.5 h13 v8.5 h-13z"/><path d="M0 2.5 l6.5 5 l6.5 -5" fill="none" stroke="#fff" stroke-width="1.2"/></svg>carla.whitfield@meridelgroup.com</li>
      <li><svg viewBox="0 0 13 13"><circle cx="6.5" cy="6.5" r="5.5" fill="none" stroke="#1a86d0" stroke-width="1.3"/><path d="M1 6.5 h11 M6.5 1 v11 M6.5 1 a3 5.5 0 0 0 0 11 a3 5.5 0 0 0 0 -11" fill="none" stroke="#1a86d0" stroke-width="1"/></svg>www.flenzo.co</li>
    </ul>
  </div>
</section>

</body>
</html>
```